Webdesign für Seminaranbieter
Zielgruppe
Die Velkor Academy bietet Kurse, Seminare & Coachings im Bereich der Kommunikation / Persönlichkeitsentwicklung an.
Folgendes Angebot besteht zur Zeit:
Seminare:
- 'Erste Schritte Dialog', eine Einführung in die Kommunikation.
- 'Sonnige Tage, ruhige Abende' zum Thema Erziehung.
- 'Zeitenwende im Herbst', zum Thema Älter werden und den Umgang damit.
Kurse:
- 'Gewaltfreie Kommunikation', Übungsgruppe
Coaching:
- Einzelsitzungen mit Hypnose
Ps: im Anhang unter 'Angabot_Vorlage.pdf' finden Sie mehr Infos zu den einezlenen Angebote.
Aufgabenstellung
Bitte berücksichtigen Sie, dass bereits ein Logo besteht (siehe Anhang).
Vom gesamteindruck her sollte die Website aufgeräumt, übersichtlich, harmonisch, freundlich & frisch wirken.
Es wäre super, wenn die Website authentisch wirkt (und weniger '0815 Business Website').
Bitte bedenken Sie, dass die Website sich an Private richtet, die sich nach einem 'strahlenderen & unbeschwerterem Lebene sehnen'.
Wir haben bereits viele Persönlichkeiten stärken können und möchten dies auch witerhin mit viel Herzblut machen.

```html
<!DOCTYPE html>
<html lang="de">
<head>
<meta charset="utf-8">
<title>Velkor Academy – Anmeldungsformular</title>
<link href="https://fonts.googleapis.com/css2?family=Raleway:wght@400;500;600&family=Montserrat:wght@400;500&family=Open+Sans:ital,wght@0,300;0,400;1,300&display=swap" rel="stylesheet">
<style>
  :root {
    --page-bg: #fcf9f8;
    --page-text: #b9b4b6;
    --page-heading: #b3aeb2;
    --accent-orange: #f26a3d;
    --accent-soft: #f4c2a6;
    --modal-head-top: #a095a8;
    --modal-head-bottom: #75677f;
    --modal-info: #8e7f8d;
    --modal-strip: #6e6180;
    --modal-form: #877682;
    --modal-foot: #6a5b78;
    --field-bg: #ffffff;
    --field-text: #8a8290;
    --white: #ffffff;
  }
  * { box-sizing: border-box; margin: 0; padding: 0; }
  html, body { width: 1200px; height: 900px; overflow: hidden; }
  body {
    background: var(--page-bg);
    font-family: "Open Sans", Arial, sans-serif;
    position: relative;
  }

  /* faded page behind the dialog */
  .page { position: absolute; inset: 0; opacity: 0.75; }
  .page__image {
    position: absolute; left: 70px; top: 80px; width: 230px; height: 380px;
    background: linear-gradient(135deg, #c9c9cb 0%, #e4e4e5 45%, #b9babd 100%);
  }
  .page__quote {
    position: absolute; left: 1030px; top: 150px;
    font-family: "Raleway", sans-serif; font-weight: 600; font-size: 15px;
    color: var(--accent-soft); white-space: nowrap;
  }
  .page__text {
    position: absolute; left: 70px; top: 520px; width: 420px;
    font-size: 14px; font-weight: 300; line-height: 21px; color: var(--page-text);
  }
  .page__text p { margin-bottom: 18px; }
  .page__text .page__cite { font-style: italic; }
  .page__text--right { left: 1040px; top: 535px; width: 160px; }
  .page__agenda {
    position: absolute; left: 72px; top: 805px;
    font-family: "Raleway", sans-serif; font-weight: 600; font-size: 21px;
    letter-spacing: 1px; color: var(--page-heading);
  }

  /* registration dialog */
  .dialog {
    position: absolute; left: 290px; top: 50px; width: 730px;
    box-shadow: 4px 6px 14px rgba(60, 40, 70, 0.35);
    font-family: "Raleway", sans-serif; color: var(--white);
  }
  .dialog__head {
    height: 130px; position: relative;
    background: linear-gradient(100deg, var(--modal-head-top), var(--modal-head-bottom));
    display: flex; align-items: center; justify-content: center;
  }
  .dialog__title { font-weight: 500; font-size: 34px; letter-spacing: 2px; }
  .dialog__close {
    position: absolute; right: 22px; top: 22px;
    font-family: "Montserrat", sans-serif; font-size: 18px; font-weight: 400;
  }
  .dialog__info {
    height: 185px; background: var(--modal-info);
    padding: 32px 0 0 150px;
  }
  .facts { display: grid; grid-template-columns: 100px auto; row-gap: 14px; font-size: 17px; }
  .facts dt { font-weight: 600; letter-spacing: 1px; }
  .facts dd { font-weight: 500; }
  .dialog__strip { height: 26px; background: var(--modal-strip); }
  .dialog__form {
    height: 190px; background: var(--modal-form);
    padding: 40px 60px 0 60px;
    display: grid; grid-template-columns: 1fr 1fr; column-gap: 56px; row-gap: 22px; align-content: start;
  }
  .field {
    height: 42px; background: var(--field-bg);
    font-family: "Montserrat", sans-serif; font-size: 14px; letter-spacing: 1.5px;
    color: var(--field-text); padding: 12px 18px; text-transform: uppercase;
  }
  .field--wide { grid-column: 1 / span 2; }
  .dialog__foot {
    height: 140px; background: var(--modal-foot);
    display: flex; align-items: center; justify-content: center;
  }
  .button-submit {
    background: var(--accent-orange); color: var(--white);
    font-family: "Montserrat", sans-serif; font-size: 14px; letter-spacing: 1.5px;
    width: 205px; height: 46px; display: flex; align-items: center; justify-content: center;
  }
</style>
</head>
<body>
  <div class="page">
    <div class="page__image" role="img" aria-label="Foto einer Armbanduhr in Grautönen"></div>
    <div class="page__quote">„Mehr Zeit in Deinem Leben“</div>
    <div class="page__text">
      <p>Zeit ist ein allgegenwärtiges Gut in unserem Alltag. Wie und wo nehmen wir sie eigentlich wahr, und was könnten? Mit welchen Fragen begegnen wir ihr?</p>
      <p>Wir setzen uns mit unserer eigenen Zeit auseinander gegenüber. Aus der passenden Haltung wächst Ruhe.</p>
      <p class="page__cite">„Älter werden ist unumgänglich, alt sein nicht.“</p>
    </div>
    <div class="page__text page__text--right">
      <p>Was bedeutet jedoch Zeit? und einmal aussteigen –</p>
      <p>Eigenschaften</p>
    </div>
    <div class="page__agenda">AGENDA</div>
  </div>

  <section class="dialog" aria-label="Anmeldungsformular">
    <header class="dialog__head">
      <h1 class="dialog__title">ANMELDUNGSFORMULAR</h1>
      <span class="dialog__close">X</span>
    </header>
    <div class="dialog__info">
      <dl class="facts">
        <dt>SEMINAR</dt><dd>Zeitenwende im Herbst</dd>
        <dt>KOSTEN</dt><dd>CHF 280.-</dd>
        <dt>ORT</dt><dd>Schloss Wendelhof</dd>
        <dt>DATUM</dt><dd>11. Mai 2019.</dd>
      </dl>
    </div>
    <div class="dialog__strip"></div>
    <div class="dialog__form">
      <div class="field">Name</div>
      <div class="field">Vorname</div>
      <div class="field field--wide">E-Mail Adresse</div>
    </div>
    <footer class="dialog__foot">
      <div class="button-submit">ANMELDEN</div>
    </footer>
  </section>
</body>
</html>
```